Banner (Template) Landing/Home Page PICTURE for my new business

I want a website Banner/ Landing/Home page / Template/ intended for a website I'm starting soon. Is this possible to have this picture and keep it for my future website? I am not completely ready to make website yet so I want an Banner.
The company will be relateed to indoor air quality & energy management controls & solutions . I like IAQ14 pic with windows and reflection of sky and trees. If IAQ14 could be put into IAQ 20, that would be interesting.with a green building or green city such as IAQ10.. See pics for example..Company name & design logo

Target Market(s)

Homeowners and building operators

Industry/Entity Type

Technical Service

Number of Pages Required

1 page

Font styles to use
Serif

Requirements
Must have
• Company Name: Larkfield Thermal Works & Services
Nice to have
• Testing Cleaning, & Controlling Your Air
• Copy of a Logo
• Mobile Web Picture
Should not have
• Your initial designs are okay to use my pics as samples. But the final product I want something creative but yet similar..Not a replica of sample pic with my company name on it

```html
<!DOCTYPE html>
<html lang="en">
<head>
<meta charset="utf-8">
<title>Larkfield Thermal Works &amp; Services</title>
<link rel="stylesheet" href="https://fonts.googleapis.com/css2?family=Raleway:wght@500;600;700&family=Open+Sans:wght@400&display=swap">
<style>
  :root {
    --sky-top: #2f7fd0;
    --sky-mid: #7db7ea;
    --sky-low: #e4f1fb;
    --white: #ffffff;
    --ink: #0d1b2a;
    --body: #1c2430;
    --accent: #1a6fb5;
    --glass-light: #a9d3f7;
    --glass-mid: #5da4ec;
    --glass-deep: #2c78d6;
    --grass-light: #7fd03a;
    --grass-deep: #2f8a14;
  }
  * { margin: 0; padding: 0; box-sizing: border-box; }
  html, body { width: 1200px; height: 720px; overflow: hidden; background: var(--white); }
  .banner {
    position: relative;
    width: 1200px;
    height: 720px;
    overflow: hidden;
    font-family: "Open Sans", sans-serif;
  }
  .sky {
    position: absolute; inset: 0;
    background:
      radial-gradient(ellipse 260px 90px at 240px 140px, rgba(255,255,255,.75), transparent 70%),
      radial-gradient(ellipse 220px 70px at 480px 30px, rgba(255,255,255,.7), transparent 70%),
      radial-gradient(ellipse 200px 80px at 1100px 150px, rgba(255,255,255,.7), transparent 70%),
      linear-gradient(180deg, var(--sky-top) 0%, var(--sky-mid) 35%, var(--sky-low) 70%, var(--white) 88%);
  }
  .towers {
    position: absolute;
    left: 914px; top: 54px; width: 250px; height: 594px;
    border-radius: 4px;
    background: linear-gradient(100deg, var(--glass-mid) 0%, var(--glass-light) 45%, var(--glass-deep) 100%);
    opacity: .9;
  }
  .house {
    position: absolute;
    left: 556px; top: 356px; width: 354px; height: 280px;
    border-radius: 8px;
    background: linear-gradient(160deg, var(--glass-light) 0%, var(--glass-mid) 50%, var(--glass-deep) 100%);
    opacity: .8;
  }
  .grass {
    position: absolute;
    left: 0; top: 606px; width: 1200px; height: 114px;
    background: linear-gradient(180deg, var(--grass-light) 0%, var(--grass-deep) 100%);
  }
  .copy { position: absolute; inset: 0; z-index: 2; }
  .brand {
    position: absolute;
    left: 76px; top: 22px;
    font-family: "Raleway", sans-serif;
    font-weight: 500;
    font-size: 88px;
    letter-spacing: 1px;
    color: var(--white);
  }
  .headline {
    position: absolute;
    left: 76px; top: 196px;
    font-family: "Raleway", sans-serif;
    font-weight: 600;
    font-size: 56px;
    line-height: 76px;
    text-transform: uppercase;
  }
  .headline-light { display: block; color: var(--white); }
  .headline-dark { display: block; color: var(--ink); font-weight: 700; }
  .intro {
    position: absolute;
    left: 77px; top: 342px;
    width: 470px;
    font-size: 18px;
    line-height: 34px;
    color: var(--body);
  }
  .read-more {
    position: absolute;
    left: 77px; top: 421px;
    width: 174px; height: 55px;
    display: flex; align-items: center; justify-content: center;
    border: 2px solid var(--accent);
    background: var(--white);
    color: var(--accent);
    font-family: "Raleway", sans-serif;
    font-weight: 700;
    font-size: 19px;
    text-decoration: none;
    text-transform: uppercase;
  }
</style>
</head>
<body>
  <main class="banner">
    <div class="sky" role="img" aria-label="Bright blue sky with soft white clouds"></div>
    <div class="towers" role="img" aria-label="Two blue glass office towers reflecting the sky"></div>
    <div class="house" role="img" aria-label="Transparent blue glass house with a hanging tag"></div>
    <div class="grass" role="img" aria-label="Strip of fresh green grass along the bottom"></div>

    <div class="copy">
      <div class="brand">LTWS</div>
      <h1 class="headline">
        <span class="headline-light">Larkfield Thermal</span>
        <span class="headline-dark">Works &amp; Services</span>
      </h1>
      <p class="intro">Mauris vel lacus vitae felis vestibulum volutpat imperdiet ac nisl Cum sociis natoque</p>
      <a class="read-more" href="#">Read More</a>
    </div>
  </main>
</body>
</html>
```